Custom Wordpress Theme - Original and Professional

We are a boutique IT consulting firm that provide small and medium business in Australia three different levels of IT service.
We are looking for a developer who will create a customised, original and professional wordpress theme. We are looking for the developer to create a professional, clean, clear and simple theme with a stylish layout, images and icons.
Our three services are: IT support | IT Services | IT Solutions and we would like to clearly differentiate the difference in each level of service in as few words as possible.
IT Support is the ad hock “call us, when you need us” service, that smaller business or those with minimal issues use.
IT service is the unlimited service, that business with existing (and well maintained) IT systems choose and is both flexible and scalable including no contracts or paperwork required.
IT solutions are the unlimited service that businesses that need new or updated infrastructure choose and it includes all the hardware, software and services with no contracts or any ongoing commitment.
The main page on the web site will attract the visitor to choose the right “service level” for their business and then we will have a dedicated page for each service and another page for a comparison (table) to compare all three services.
Lastly we will need a contact us page that has both office locations (Sydney and Melbourne), contact phone numbers and an email form.
Items we are focused on for this project are: 1. Images, 2.Icons 3. Layout.
In summary we are looking for a custom WordPress theme into a 6 page (Home, IT Support, IT Services, IT Solutions, Compare Service levels and Contact us) website. The design must include relevant images and icons and be clear, simple, professional and sleek.

Thank you for your time and creativity and I look forward to working with you!

Target Market(s)

Small and Medium businesses in Australia

Industry/Entity Type

Cobaltline

Requirements
Must have
• - 6 Pages layout: Home, IT support, IT services, IT Solutions, Compare service levels and Contact us
- Images, Layout and Icons.
- Clean, Clear, Simple, Elegant, Stylish.
Nice to have
• - Some text (if possible but not required).
Should not have
• - Complexity.
- Confusing layout.
- Generic non matching images and icons.

```html
<!DOCTYPE html>
<html lang="en">
<head>
<meta charset="utf-8">
<title>Cobaltline — IT Support</title>
<link rel="stylesheet" href="https://fonts.googleapis.com/css2?family=Source+Sans+3:wght@300;400;600&display=swap">
<style>
  :root {
    --navy-dark: #021a4c;
    --navy: #0b3577;
    --heading: #0e2b63;
    --text: #6b6b6b;
    --text-dark: #555;
    --orange: #f08a2b;
    --date: #f0642a;
    --rule: #e6e6e6;
    --footer-bg: #f7f7f7;
    --icon: #5a5a5a;
    --white: #fff;
  }
  * { margin: 0; padding: 0; box-sizing: border-box; }
  html, body { width: 1200px; height: 999px; overflow: hidden; background: var(--white); }
  body { position: relative; font-family: "Source Sans 3", "Helvetica Neue", Arial, sans-serif; color: var(--text); }

  .site-header {
    position: absolute; left: 0; top: 0; width: 1200px; height: 115px;
    background: linear-gradient(to bottom, var(--navy) 0%, var(--navy-dark) 100%);
  }
  .brand { position: absolute; left: 90px; top: 30px; font-size: 44px; font-weight: 400; color: var(--white); line-height: 1; }
  .phone { position: absolute; right: 88px; top: 12px; display: flex; align-items: center; gap: 4px; color: var(--white); font-size: 23px; }
  .main-nav { position: absolute; right: 87px; top: 63px; display: flex; }
  .main-nav a { color: var(--white); text-decoration: none; font-size: 18.5px; padding: 0 13px; border-left: 1px solid rgba(255,255,255,.35); line-height: 22px; }
  .main-nav a:first-child { border-left: none; }
  .main-nav a:last-child { padding-right: 0; }

  .hero { position: absolute; left: 84px; top: 115px; width: 1039px; height: 257px; }
  .hero-photo {
    position: absolute; inset: 0;
    background: linear-gradient(to right, #5a5f66 0%, #8a8f96 18%, #b9a08c 34%, #d7dde6 52%, #eef2f6 70%, #dfe4ea 100%);
  }
  .hero-caption { position: absolute; left: 605px; top: 94px; color: var(--heading); }
  .hero-caption h2 { font-size: 33px; font-weight: 400; line-height: 1.1; }
  .hero-caption p { font-size: 21px; font-weight: 400; margin-top: 4px; }
  .hero-rule { position: absolute; left: 0; top: 372px; width: 1200px; height: 1px; background: var(--rule); }

  .content { position: absolute; left: 100px; top: 405px; width: 685px; }
  .content h1 { font-size: 29px; font-weight: 400; color: var(--heading); line-height: 1; margin-bottom: 8px; }
  .content p { font-size: 14.5px; font-weight: 300; line-height: 22.5px; margin-bottom: 8px; }
  .gallery { display: flex; gap: 17px; margin: 17px 0 17px 5px; }
  .gallery div { width: 212px; height: 105px; border-radius: 3px; }
  .gallery .office { background: linear-gradient(to right, #e9f1f8, #cfdce8 50%, #eef3f8); }
  .gallery .cabling { width: 215px; background: linear-gradient(135deg, #6b5a4e, #3e7fae 55%, #2f5f86); }
  .content .body-long { margin-left: 3px; }

  .news { position: absolute; left: 828px; top: 408px; width: 290px; }
  .news h2 { font-size: 28px; font-weight: 300; color: var(--orange); line-height: 1; margin-bottom: 14px; }
  .news-item { margin-left: 3px; margin-bottom: 30px; }
  .news-item h3 { font-size: 18px; font-weight: 400; color: var(--text-dark); margin-bottom: 6px; }
  .news-item p { font-size: 14px; font-weight: 300; line-height: 22.5px; color: var(--text-dark); margin-bottom: 8px; }
  .news-item time { font-size: 13.5px; font-weight: 300; color: var(--date); }

  .site-footer { position: absolute; left: 0; top: 870px; width: 1200px; height: 129px; background: var(--footer-bg); border-top: 1px solid #eee; }
  .footer-nav { position: absolute; left: 80px; top: 42px; display: flex; }
  .footer-nav a { color: var(--text-dark); text-decoration: none; font-size: 16.5px; }
  .footer-nav span { color: var(--text-dark); font-size: 16.5px; padding: 0 11px; }
  .copyright { position: absolute; left: 80px; top: 79px; font-size: 12.5px; color: var(--text-dark); font-weight: 300; }
  .social { position: absolute; left: 964px; top: 56px; display: flex; gap: 5px; }
  .social span { width: 32px; height: 32px; border-radius: 50%; background: var(--icon); display: block; }
</style>
</head>
<body>
  <header class="site-header">
    <div class="brand">Cobaltline</div>
    <div class="phone">
      <svg width="20" height="22" viewBox="0 0 20 22" aria-hidden="true"><path fill="#fff" d="M4 1c1-.6 2 .2 2.6 1.2l2 3.4c.5.9.2 1.8-.6 2.3l-1.3.8c.8 2.5 2.4 4.9 4.4 6.6l1.3-.8c.8-.5 1.8-.3 2.3.5l2.2 3.2c.6.9.5 2-.4 2.6-1.6 1.1-3.6 1.6-5.4.6C6.5 18.7 3 13.6 1.6 8.2 1 6 2 2.3 4 1z"/></svg>
      555.0142.3870
    </div>
    <nav class="main-nav">
      <a href="#">Home</a><a href="#">IT support</a><a href="#">IT services</a><a href="#">IT Solutions</a><a href="#">Compare service levels</a><a href="#">Contact us</a>
    </nav>
  </header>

  <section class="hero">
    <div class="hero-photo" role="img" aria-label="IT technician standing beside a server rack in an office"></div>
    <div class="hero-caption">
      <h2>IT Support</h2>
      <p>Donec scelerisque leo risus</p>
    </div>
  </section>
  <div class="hero-rule"></div>

  <main class="content">
    <h1>IT Support</h1>
    <p>Nunc tempus felis vitae urna. Vivamus porttitor, g, purus nisi eleifend libero, a tempus libero lectus feugiat felis. Morbi diam mauris, viverra in, gravida eu, mattis in, ante. Morbi eget arcu.</p>
    <p>Phasellus felis dolor, scelerisque a, tempus eget, lobortis id, libero. Donec scelerisque leo ac risus. Praesent sit amet est. In dictum, dolor eu dictum porttitor, enim felis viverra mi eget luctus massa purus quis odio.</p>
    <div class="gallery">
      <div class="office" role="img" aria-label="Business consultant in a bright office"></div>
      <div class="cabling" role="img" aria-label="Technician working on blue network cabling"></div>
    </div>
    <p class="body-long">Phasellus felis dolor, scelerisque a, tempus eget, lobortis id, libero. Donec scelerisque leo ac risus. Praesent sit amet est. In dictum, dolor eu dictum porttitor, enim felis viverra mi, eget luctus massa purus quis odio. Etiam nulla massa, pharetra facilisis, volutpat in, imperdiet sit amet, sem. Aliquam nec erat at purus cursus interdum. Vestibulum ligula augue, bibendum accumsan, vestibulum ut, commodo a, mi. Morbi ornare gravida elit. Integer congue, augue et malesuada iaculis, ipsum dui aliquet felis, at cursus magna nisl nec elit. viverra. Duis sed tellus et tortor vestibulum gravida. Praesent elementum elit at tellus.</p>
  </main>

  <aside class="news">
    <h2>In the News</h2>
    <article class="news-item">
      <h3>Fusce ultricies orci</h3>
      <p>Morbi magna magna, tincidunt a, mattis non, imperdiet vitae, tellus. Sed odio est, auctor ac, sollicitudin in, consequat vitae</p>
      <time>Tuesday, 19 June 2012 16:47</time>
    </article>
    <article class="news-item">
      <h3>Etiam est nunc</h3>
      <p>Morbi magna magna, tincidunt a, mattis non, imperdiet vitae, tellus. Sed odio est, auctor ac, sollicitudin in, consequat vitae</p>
      <time>Saturday, 09 June 2012 13:58</time>
    </article>
  </aside>

  <footer class="site-footer">
    <nav class="footer-nav">
      <a href="#">Home</a><span>|</span><a href="#">IT support</a><span>|</span><a href="#">IT services</a><span>|</span><a href="#">IT Solutions</a><span>|</span><a href="#">Compare service levels</a><span>|</span><a href="#">Contact us</a>
    </nav>
    <p class="copyright">Copyright © 2013 Company Name.&nbsp; All right reserved</p>
    <div class="social" aria-label="Social links">
      <span></span><span></span><span></span><span></span>
    </div>
  </footer>
</body>
</html>
```